Business Card Trio Design

We need a set of business cards that all match but are not identical. We need one generic for the business and one for each of the two owners. We would like the cards to be similar to each other, but not identical. We have a logo and the colors of the logo are painstakingly chosen so if blue or green is used, we prefer our specific blue and green. Our logo pops better on a black background as well. We are open to double-sided, but it is not the top choice. We would love some either gold or silver accents that are in a foiled appearance. We sell uniforms (scrubs, culinary, EMT, police, fire, business, all types except kids and sports), shoes, equipment, and accessories. We also have quorvalink, mavelgrid, lumopixel, and yondrel that we would like to have them follow and we offer zembrix in the store we would like the card to also advertise.

```html
<!DOCTYPE html>
<html lang="en">
<head>
<meta charset="utf-8">
<title>Verdant Wear Business Card</title>
<link href="https://fonts.googleapis.com/css2?family=Montserrat:wght@400;500;600;700&display=swap" rel="stylesheet">
<style>
  :root {
    --stage: #3e3e40;
    --brand-green: #009570;
    --brand-green-deep: #038a5f;
    --brand-blue: #86a4c3;
    --paper: #ffffff;
    --ink-light: #ffffff;
  }
  html, body {
    margin: 0;
    padding: 0;
    width: 1200px;
    height: 1200px;
    overflow: hidden;
    background: var(--stage);
    font-family: "Montserrat", sans-serif;
  }
  .canvas {
    position: relative;
    width: 1200px;
    height: 1200px;
  }
  .card {
    position: absolute;
    left: 150px;
    width: 900px;
    height: 514px;
    border-radius: 30px;
    overflow: hidden;
    box-shadow: 0 14px 30px rgba(0,0,0,0.35);
  }
  .card-front { top: 56px; background: var(--paper); }
  .card-back { top: 630px; background: var(--brand-green-deep); }
  .card-art {
    position: absolute;
    inset: 0;
    width: 100%;
    height: 100%;
  }
  .identity {
    position: absolute;
    left: 70px;
    top: 150px;
    padding-left: 22px;
    border-left: 6px solid var(--ink-light);
    color: var(--ink-light);
  }
  .identity-name {
    margin: 0;
    font-size: 46px;
    font-weight: 600;
    letter-spacing: 1px;
    line-height: 1;
  }
  .identity-title {
    margin: 8px 0 0;
    font-size: 22px;
    font-weight: 400;
    letter-spacing: 1px;
  }
  .contact-list {
    position: absolute;
    left: 70px;
    top: 290px;
    margin: 0;
    padding: 0;
    list-style: none;
    color: var(--ink-light);
    font-size: 21px;
    font-weight: 400;
  }
  .contact-item {
    display: flex;
    align-items: center;
    gap: 14px;
    height: 40px;
  }
  .contact-icon {
    width: 24px;
    height: 24px;
    flex: none;
  }
  .contact-spacer { width: 24px; flex: none; }
  .wordmark {
    position: absolute;
    display: flex;
    align-items: center;
    gap: 18px;
    font-family: "Montserrat", sans-serif;
    font-weight: 600;
    letter-spacing: 4px;
    line-height: 1.05;
  }
  .wordmark-front {
    right: 70px;
    top: 150px;
    color: var(--brand-green);
    font-size: 38px;
  }
  .wordmark-back {
    left: 50%;
    top: 50%;
    transform: translate(-50%, -50%);
    color: var(--ink-light);
    font-size: 60px;
    gap: 28px;
  }
  .wordmark-dot {
    flex: none;
    border-radius: 50%;
    background: currentColor;
  }
  .wordmark-front .wordmark-dot { width: 70px; height: 70px; }
  .wordmark-back .wordmark-dot { width: 110px; height: 110px; }
</style>
</head>
<body>
<main class="canvas">

  <section class="card card-front" aria-label="Business card front">
    <svg class="card-art" viewBox="0 0 900 514" preserveAspectRatio="none" aria-hidden="true">
      <path d="M0,0 H260 C520,70 590,300 560,514 H0 Z" fill="var(--brand-green)"/>
      <path d="M282,0 C560,80 640,300 612,514 H588 C610,300 540,90 268,0 Z" fill="var(--brand-blue)"/>
    </svg>

    <div class="identity">
      <h1 class="identity-name">ARLO PENN</h1>
      <p class="identity-title">CEO | FOUNDER</p>
    </div>

    <ul class="contact-list">
      <li class="contact-item">
        <svg class="contact-icon" viewBox="0 0 24 24" aria-hidden="true"><path d="M6.6 10.8a15 15 0 0 0 6.6 6.6l2.2-2.2a1 1 0 0 1 1-.25 11.4 11.4 0 0 0 3.6.57 1 1 0 0 1 1 1V20a1 1 0 0 1-1 1A17 17 0 0 1 3 4a1 1 0 0 1 1-1h3.5a1 1 0 0 1 1 1c0 1.25.2 2.45.57 3.57a1 1 0 0 1-.25 1z" fill="#fff"/></svg>
        <span>555-014-2290</span>
      </li>
      <li class="contact-item">
        <svg class="contact-icon" viewBox="0 0 24 24" aria-hidden="true"><rect x="2" y="5" width="20" height="14" rx="1" fill="none" stroke="#fff" stroke-width="2"/><polyline points="2,5 12,13 22,5" fill="none" stroke="#fff" stroke-width="2"/></svg>
        <span>desk@verdantwear.com</span>
      </li>
      <li class="contact-item">
        <svg class="contact-icon" viewBox="0 0 24 24" aria-hidden="true"><circle cx="12" cy="12" r="10" fill="none" stroke="#fff" stroke-width="2"/><ellipse cx="12" cy="12" rx="4.5" ry="10" fill="none" stroke="#fff" stroke-width="1.6"/><line x1="2" y1="12" x2="22" y2="12" stroke="#fff" stroke-width="1.6"/></svg>
        <span>www.verdantwear.com</span>
      </li>
      <li class="contact-item">
        <span class="contact-spacer"></span>
        <span>lumopixel | quorvalink</span>
      </li>
    </ul>

    <div class="wordmark wordmark-front">
      <span class="wordmark-dot"></span>
      <span>VERDANT<br>WEAR</span>
    </div>
  </section>

  <section class="card card-back" aria-label="Business card back">
    <div class="wordmark wordmark-back">
      <span class="wordmark-dot"></span>
      <span>VERDANT<br>WEAR</span>
    </div>
  </section>

</main>
</body>
</html>
```